Financial planning wealth advisor Business Card

We have a finanancial advisory that caters to high net worth and business owner clients. We would like a card that works with our entire style. Please visit out website larkfieldcapitalpartners.com to get a look and feel.... VERY OPEN to interesting and unique designs that have cutouts, fold overs, anything to capture interest...

Requirements, info must be the following:

Larkfield Capital Partners (with Logo)
Investments | Insurance | Retirement | Education | Estate | Business Planning

Nora Vesk Albright, CFP, MSFS, AEP
Principal

555-207-8160 (Main)
555-382-9045 (Cell)
ealbright@larkfieldcapitalpartners.com

Central Location:
218 W Palomar Suite 1400
El Paso TX 79814

West Location:
6132 Millbrook Lane SuiteB
El Paso TX 79836

larkfieldcapitalpartners.com

DISCLOSURES (Back of Card)
Eleanor Vesk Albright, CFP, MSFS, AEP, a Registered Representative offering securities through TORVANE Brokerage LLC. 218 W Palomar Suite 1400 El Paso TX 79814 555-619-4720. Member NARFIN/SIPRA, a licensed insurance agency.

*Financial Adviser offering investment advisory services through Harrow Advisory, LLC, a Registered Investment Advisor.

Larkfield Capital Partners is not owned or operated by TORVANE Brokerage LLC or its affiliates.

Target Market(s)

High end affluent or ultra rich clientele

Industry/Entity Type

Financial Planning

Font styles to use
Decorative

Requirements
Must have
• Needs to have something that focuses our services. :33 bellow for our original business card.

```html
<!DOCTYPE html>
<html lang="en">
<head>
<meta charset="utf-8">
<title>Larkfield Capital Partners Business Card</title>
<link rel="stylesheet" href="https://fonts.googleapis.com/css2?family=Arimo:wght@400;700&display=swap">
<style>
  :root {
    --bg: #2b2b2d;
    --gold: #c9a567;
    --gold-deep: #b8914f;
    --navy: #1c2f6b;
    --navy-deep: #15245a;
    --white: #ffffff;
    --ink-navy: #1f3170;
  }
  * { box-sizing: border-box; margin: 0; padding: 0; }
  html, body { width: 1200px; height: 950px; overflow: hidden; }
  body {
    background: var(--bg);
    font-family: "Arimo", Arial, sans-serif;
    position: relative;
  }
  .card {
    position: absolute;
    left: 250px;
    width: 700px;
    height: 400px;
    overflow: hidden;
    box-shadow: 0 10px 30px rgba(0,0,0,.45);
  }

  /* Back of card */
  .card-back {
    top: 45px;
    background: var(--gold);
    color: var(--white);
    text-align: center;
    padding: 0 46px;
  }
  .back-brand {
    display: flex;
    align-items: center;
    justify-content: center;
    gap: 14px;
    margin-top: 100px;
    font-size: 32px;
    font-weight: 400;
    letter-spacing: 2px;
    text-transform: uppercase;
    white-space: nowrap;
  }
  .brand-dot {
    width: 16px; height: 16px; border-radius: 50%;
    background: currentColor;
    flex: none;
  }
  .services {
    margin-top: 56px;
    font-size: 15px;
    font-weight: 700;
    letter-spacing: .2px;
  }
  .disclosure {
    margin-top: 18px;
    font-size: 12.5px;
    line-height: 1.45;
  }

  /* Front of card */
  .card-front {
    top: 505px;
    background: var(--white);
  }
  .front-shape { position: absolute; inset: 0; }
  .front-brand {
    position: absolute;
    right: 44px;
    top: 52px;
    display: flex;
    align-items: center;
    gap: 12px;
    color: var(--ink-navy);
    font-size: 30px;
    font-weight: 400;
    letter-spacing: 2px;
    text-transform: uppercase;
    white-space: nowrap;
  }
  .front-brand .brand-dot { background: var(--gold); }
  .identity {
    position: absolute;
    left: 40px;
    top: 108px;
    color: var(--ink-navy);
  }
  .identity .name { font-size: 27px; font-weight: 700; }
  .identity .credentials { font-size: 17px; font-weight: 700; margin-top: 6px; }
  .identity .role { font-size: 16px; color: var(--gold); margin-top: 12px; }

  .contacts {
    position: absolute;
    right: 34px;
    top: 176px;
    list-style: none;
    color: var(--white);
    font-size: 15.5px;
    text-align: right;
  }
  .contacts li {
    display: flex;
    align-items: center;
    justify-content: flex-end;
    gap: 8px;
    height: 23px;
  }
  .contacts svg { width: 15px; height: 15px; flex: none; }

  .locations {
    position: absolute;
    left: 40px;
    bottom: 24px;
    color: var(--white);
    font-size: 15px;
    line-height: 1.22;
  }
  .locations .label { color: var(--gold); font-weight: 700; }
</style>
</head>
<body>

  <section class="card card-back" aria-label="Back of card">
    <div class="back-brand"><span class="brand-dot"></span>Larkfield Capital Partners</div>
    <p class="services">Investments | Insurance | Retirement | Education | Estate | Business Planning</p>
    <p class="disclosure">
      Eleanor Vesk Albright, CFP, MSFS, AEP, a Registered Representative offering securities
      through TORVANE Brokerage LLC. 218 W Palomar Suite 1400 El Paso TX 79814 555-619-4720.
      Member NARFIN/SIPRA, a licensed insurance agency. *Financial Adviser offering investment
      advisory services through Harrow Advisory, LLC, a Registered Investment Advisor. Larkfield
      Capital Partners is not owned or operated by TORVANE Brokerage LLC or its affiliates.
    </p>
  </section>

  <section class="card card-front" aria-label="Front of card">
    <svg class="front-shape" viewBox="0 0 700 400" width="700" height="400" aria-hidden="true">
      <path d="M0 250 Q330 195 700 140 L700 400 L0 400 Z" fill="var(--navy)"/>
      <path d="M34 240 Q340 180 700 122 L700 132 Q340 192 40 250 Z" fill="var(--gold)"/>
      <path d="M10 246 L42 232 L40 256 Z" fill="var(--gold)"/>
    </svg>

    <div class="front-brand"><span class="brand-dot"></span>Larkfield Capital Partners</div>

    <div class="identity">
      <p class="name">Nora Vesk Albright</p>
      <p class="credentials">CFP, MSFS, AEP</p>
      <p class="role">Principal</p>
    </div>

    <ul class="contacts">
      <li>555-207-8160
        <svg viewBox="0 0 16 16"><path fill="var(--gold)" d="M3 2h3l1 3-2 1.2a8 8 0 0 0 4.8 4.8L11 9l3 1v3a1.5 1.5 0 0 1-1.5 1.5A11.5 11.5 0 0 1 1.5 3.5 1.5 1.5 0 0 1 3 2z"/></svg>
      </li>
      <li>555-382-9045
        <svg viewBox="0 0 16 16"><rect x="4" y="1" width="8" height="14" rx="1.5" fill="var(--gold)"/><rect x="5.5" y="3" width="5" height="8" fill="var(--navy)"/></svg>
      </li>
      <li>ealbright@larkfieldcapitalpartners.com
        <svg viewBox="0 0 16 16"><rect x="1" y="3" width="14" height="10" rx="1" fill="var(--gold)"/><path d="M1.5 3.8 8 9l6.5-5.2" stroke="var(--navy)" stroke-width="1.3" fill="none"/></svg>
      </li>
      <li>larkfieldcapitalpartners.com
        <svg viewBox="0 0 16 16"><circle cx="8" cy="8" r="7" fill="var(--gold)"/><path d="M1 8h14M8 1c-3 3.5-3 10.5 0 14M8 1c3 3.5 3 10.5 0 14" stroke="var(--navy)" stroke-width="1.1" fill="none"/></svg>
      </li>
    </ul>

    <div class="locations">
      <p class="label">Central Location:</p>
      <p>218 W Palomar Suite 1400</p>
      <p>El Paso TX 79814</p>
      <p class="label">West Location:</p>
      <p>6132 Millbrook Lane SuiteB</p>
      <p>El Paso TX 79836</p>
    </div>
  </section>

</body>
</html>
```